Business Card Design Project

We need a business card design for a new boutique consulting company, TivaConsulting. Our new logo has just been designed and we are looking for simple, clean looking business cards. Logo attached

Industry/Entity Type

Boutique

Requirements
Must have
• There must be room for each card to have the following details:
Name
Title
Address - 2 lines
Phone number
Email address
Website address

Nice to have
• May have something on the back of the buisness card - emphasing the word "Tiva".

```html
<!DOCTYPE html>
<html lang="en">
<head>
<meta charset="utf-8">
<title>TivaConsulting Business Cards</title>
<link rel="stylesheet" href="https://fonts.googleapis.com/css2?family=Questrial&display=swap">
<style>
  :root {
    --backdrop: #e9e6e1;
    --card-white: #ffffff;
    --card-dark: #333333;
    --brand-green: #6cbf45;
    --text-dark: #2b2b2b;
    --text-grey: #9a9a9a;
    --band-text: #ffffff;
  }
  * { margin: 0; padding: 0; box-sizing: border-box; }
  html, body {
    width: 1200px;
    height: 615px;
    overflow: hidden;
    background: var(--backdrop);
    font-family: "Questrial", "Century Gothic", sans-serif;
  }
  .stage { position: relative; width: 1200px; height: 615px; }

  .card {
    position: absolute;
    width: 553px;
    height: 337px;
    border-radius: 20px;
    overflow: hidden;
    box-shadow: 0 3px 10px rgba(0,0,0,0.18);
  }

  /* Front */
  .card-front { left: 31px; top: 31px; background: var(--card-white); }
  .front-wordmark {
    position: absolute;
    right: 18px;
    top: 8px;
    font-size: 44px;
    letter-spacing: -0.5px;
    color: var(--brand-green);
  }
  .holder-name {
    position: absolute;
    left: 17px;
    top: 130px;
    font-size: 31px;
    letter-spacing: -0.4px;
    color: var(--text-dark);
  }
  .holder-title {
    position: absolute;
    left: 17px;
    top: 166px;
    font-size: 20px;
    color: var(--text-grey);
  }
  .contact-list {
    position: absolute;
    left: 280px;
    top: 194px;
    list-style: none;
    font-size: 16.5px;
    line-height: 20px;
    color: var(--text-dark);
  }
  .contact-list li { display: flex; }
  .contact-label { width: 16px; color: var(--brand-green); }
  .web-band {
    position: absolute;
    left: 0;
    bottom: 0;
    width: 100%;
    height: 50px;
    background: var(--card-dark);
    color: var(--band-text);
    font-size: 25px;
    text-align: center;
    line-height: 48px;
    letter-spacing: 0.3px;
  }

  /* Back */
  .card-back { left: 616px; top: 246px; background: var(--card-dark); }
  .back-wordmark {
    position: absolute;
    left: 0;
    top: 0;
    width: 100%;
    height: 100%;
    display: flex;
    align-items: center;
    justify-content: center;
    gap: 14px;
    font-size: 64px;
    letter-spacing: -0.8px;
    color: var(--brand-green);
  }
  .brand-dot {
    width: 22px;
    height: 22px;
    border-radius: 50%;
    background: var(--brand-green);
  }
</style>
</head>
<body>
<main class="stage">
  <section class="card card-front" aria-label="Business card front">
    <div class="front-wordmark">TivaConsulting</div>
    <h1 class="holder-name">Maren Holloway</h1>
    <p class="holder-title">Title/Position</p>
    <ul class="contact-list">
      <li><span class="contact-label">a</span><span>PO Box 31-408 Harbour Lane,</span></li>
      <li><span class="contact-label"></span><span>Wellington, NZ 6011</span></li>
      <li><span class="contact-label">p</span><span>04 555 0182</span></li>
      <li><span class="contact-label">e</span><span>info@tivaconsulting.co.nz</span></li>
    </ul>
    <div class="web-band">www.tivaconsulting.co.nz</div>
  </section>

  <section class="card card-back" aria-label="Business card back">
    <div class="back-wordmark">
      <span class="brand-dot" aria-hidden="true"></span>
      <span>TivaConsulting</span>
    </div>
  </section>
</main>
</body>
</html>
```